Volt menders . Energy efficiency improvement for residential and commercial/industrial

Logo needed for “ volt menders .com “ website. Conduct energy audits and provide consulting about efficiency improvements . I will provide content for pages about 10 pages . Get customer serway and store information .
Some pages will be copied from Lumacrestbyx.com

```html
<!DOCTYPE html>
<html lang="en">
<head>
<meta charset="utf-8">
<title>Volt Menders</title>
<link rel="stylesheet" href="https://fonts.googleapis.com/css2?family=Lato:ital,wght@0,400;0,700;0,900;1,400&display=swap">
<style>
:root{
  --blue:#1f4fd1;
  --blue-dark:#1a3fb0;
  --green:#5aab4f;
  --green-dark:#4a9a41;
  --ink:#1d1d1d;
  --muted:#666;
  --line:#cfcfcf;
  --white:#fff;
}
*{margin:0;padding:0;box-sizing:border-box}
html,body{width:1200px;height:2734px;overflow:hidden;background:#fff}
body{position:relative;font-family:'Lato',sans-serif;color:var(--ink)}
.abs{position:absolute}

.hero{left:0;top:0;width:1200px;height:564px;
  background:linear-gradient(100deg,#7a6f5c 0%,#c9b48c 35%,#d9cdb5 55%,#8f8f8a 80%,#6c6c6c 100%)}
.hero-topline{left:0;top:0;width:1200px;height:3px;background:var(--blue)}
.brand{left:143px;top:38px;display:flex;align-items:center;gap:12px;font-weight:900;font-size:34px;color:var(--blue)}
.brand-mark{width:36px;height:36px;border-radius:50%;background:var(--blue)}
.nav{left:528px;top:44px;display:flex;gap:27px;font-size:15px;font-weight:700;color:#1d1d1d}
.nav .active{border-bottom:2px solid var(--green);padding-bottom:4px}
.search{left:1023px;top:39px;width:32px;height:32px;border-radius:50%;background:var(--blue)}
.hero-title{left:664px;top:176px;font-weight:900;font-size:86px;line-height:84px;color:#fff;text-shadow:0 2px 6px rgba(0,0,0,.35);letter-spacing:-1px}
.btn{display:flex;align-items:center;justify-content:center;border-radius:32px;color:#fff;font-weight:700}
.hero-btn{left:670px;top:379px;width:202px;height:63px;background:var(--green);font-size:19px;font-weight:400}
.dots{left:560px;top:509px;display:flex;gap:8px}
.dots span{width:10px;height:10px;border-radius:50%;background:#fff}
.dots span.on{background:transparent;border:2px solid #fff}

.quote-band{left:0;top:564px;width:1200px;height:109px;background:var(--blue);color:#fff;padding:27px 0 0 171px;font-size:15px;line-height:27px;font-style:italic}
.quote-band em{font-style:normal;font-size:17px}

.services-bg{left:0;top:673px;width:1200px;height:645px;background:linear-gradient(180deg,#fff 0%,#f4f5f6 60%,#eceeee 100%)}
.section-title{left:0;width:1200px;text-align:center;font-weight:900;font-size:50px;letter-spacing:-1px;color:var(--ink)}
.svc{width:460px}
.svc h3{font-size:23px;font-weight:700;line-height:27px;margin-bottom:14px}
.svc p{font-size:14px;line-height:22px;color:var(--muted);width:280px}
.svc a{display:block;margin-top:14px;font-size:15px;font-weight:700;color:var(--blue);text-decoration:none}
.ring{width:132px;height:132px}

.about{left:0;top:1318px;width:1200px;height:488px;background:linear-gradient(90deg,#5fae53,#5aab4f 60%,#4f9f45)}
.diamond-frame{left:144px;top:1410px;width:448px;height:497px;background:var(--green-dark);clip-path:polygon(50% 0,100% 45%,50% 100%,0 45%)}
.diamond-photo{left:145px;top:1410px;width:446px;height:446px;clip-path:polygon(50% 0,100% 50%,50% 100%,0 50%);
  background:linear-gradient(135deg,#bfd8ee 0%,#dfe7ef 40%,#8a9099 75%,#c9a68e 100%)}
.about-title{left:646px;top:1372px;font-size:50px;font-weight:900;color:#fff;letter-spacing:-1px}
.about-text{left:646px;top:1449px;width:412px;font-size:14px;line-height:24px;color:#fff}
.about-btn{left:646px;top:1692px;width:156px;height:49px;background:var(--blue);font-size:15px;font-weight:400}

.field{border:1px solid var(--line);background:#fff;font-size:14px;color:#333;padding:0 29px;display:flex;align-items:center}
.field.msg{align-items:flex-start;padding-top:20px}
.submit{left:491px;top:2318px;width:218px;height:58px;background:var(--blue);font-size:17px}

.footer-line{left:0;top:2454px;width:1200px;height:9px;background:var(--green)}
.footer{left:0;top:2463px;width:1200px;height:271px;background:linear-gradient(180deg,#2150d4,#1e47c4)}
.ficon{width:40px;height:40px;border-radius:50%;border:1.5px solid rgba(255,255,255,.8)}
.ftext{font-size:14px;line-height:22px;color:#fff}
.fnav{left:0;top:2591px;width:1200px;display:flex;justify-content:center;gap:32px;font-size:19px;font-weight:700;color:#fff}
.fdivider{left:0;top:2648px;width:1200px;height:1px;background:rgba(255,255,255,.25)}
.copy{left:144px;top:2687px;font-size:13px;color:#fff}
.social{left:920px;top:2679px;display:flex;gap:6px}
.social span{width:30px;height:30px;border-radius:50%;border:1.5px solid rgba(255,255,255,.85)}
</style>
</head>
<body>

<div class="abs hero" role="img" aria-label="Photo of an engineer in a hard hat and safety vest pointing at an industrial power plant"></div>
<div class="abs hero-topline"></div>
<div class="abs brand"><span class="brand-mark"></span>Volt Menders</div>
<nav class="abs nav"><span class="active">Home</span><span>About</span><span>Services</span><span>Case Studies</span><span>News</span><span>Contact us</span></nav>
<div class="abs search"><svg width="32" height="32" viewBox="0 0 32 32"><circle cx="15" cy="15" r="4" fill="none" stroke="#fff" stroke-width="2"/><line x1="18" y1="18" x2="21" y2="21" stroke="#fff" stroke-width="2"/></svg></div>
<h1 class="abs hero-title">VOLT<br>MENDERS</h1>
<div class="abs btn hero-btn">GET STARTED</div>
<div class="abs dots"><span></span><span></span><span class="on"></span><span></span><span></span></div>

<div class="abs quote-band">Volt menders' Energy Management System was made for energy efficiency projects. It helps identify the best opportunities and creates the<br>benchmarking, verification and ROI data to justify the projects and apply for the rebates!" &nbsp;<em>— Energy Efficiency Engineer</em></div>

<div class="abs services-bg" role="img" aria-label="Faint sketch of wind turbines and solar panels"></div>
<h2 class="abs section-title" style="top:760px">OUR SERVICES</h2>

<svg width="0" height="0" style="position:absolute">
  <defs><linearGradient id="ringGrad" x1="0" y1="0" x2="1" y2="1"><stop offset="0" stop-color="#1f4fd1"/><stop offset="0.55" stop-color="#2a6fa8"/><stop offset="1" stop-color="#5aab4f"/></linearGradient></defs>
</svg>

<svg class="abs ring" style="left:143px;top:902px" viewBox="0 0 132 132"><circle cx="66" cy="66" r="62" fill="#fff" stroke="url(#ringGrad)" stroke-width="4"/><rect x="38" y="38" width="56" height="56" rx="6" fill="#e6ecfa" role="img" aria-label="Audit document icon"/></svg>
<div class="abs svc" style="left:297px;top:898px"><h3>Energy audits</h3><p>Lorem ipsum dolor sit amet, consectetur adipiscing ed do eiusmod tempor incididunt ut labore et dolore magna aliqua.</p><a>READ MORE</a></div>

<svg class="abs ring" style="left:645px;top:902px" viewBox="0 0 132 132"><circle cx="66" cy="66" r="62" fill="#fff" stroke="url(#ringGrad)" stroke-width="4"/><rect x="38" y="38" width="56" height="56" rx="6" fill="#e6ecfa" role="img" aria-label="Consulting team icon"/></svg>
<div class="abs svc" style="left:799px;top:898px"><h3>Consulting</h3><p>Lorem ipsum dolor sit amet, consectetur adipiscing ed do eiusmod tempor incididunt ut labore et dolore magna aliqua.</p><a>READ MORE</a></div>

<svg class="abs ring" style="left:143px;top:1102px" viewBox="0 0 132 132"><circle cx="66" cy="66" r="62" fill="#fff" stroke="url(#ringGrad)" stroke-width="4"/><rect x="38" y="38" width="56" height="56" rx="6" fill="#e6ecfa" role="img" aria-label="House icon"/></svg>
<div class="abs svc" style="left:297px;top:1098px"><h3>Energy efficiency<br>for residential</h3><p>Lorem ipsum dolor sit amet, consectetur adipiscing ed do eiusmod tempor</p><a>READ MORE</a></div>

<svg class="abs ring" style="left:645px;top:1102px" viewBox="0 0 132 132"><circle cx="66" cy="66" r="62" fill="#fff" stroke="url(#ringGrad)" stroke-width="4"/><rect x="38" y="38" width="56" height="56" rx="6" fill="#e6ecfa" role="img" aria-label="Commercial building plan icon"/></svg>
<div class="abs svc" style="left:799px;top:1098px"><h3>Energy efficiency<br>for Commercial</h3><p>Lorem ipsum dolor sit amet, consectetur adipiscing ed do eiusmod tempor</p><a>READ MORE</a></div>

<div class="abs about" role="img" aria-label="Green-tinted photo of a worker with a tablet at an industrial site"></div>
<div class="abs diamond-frame"></div>
<div class="abs diamond-photo" role="img" aria-label="Photo of a hand on a laptop showing an energy efficiency rating chart"></div>
<h2 class="abs about-title">ABOUT US</h2>
<p class="abs about-text">Volt menders provides a unique Energy Monitoring, Operations Management, and Engineering Support solution using advanced wireless IoT technology to help companies understand and effectively manage energy use and equipment operations to achieve efficiency, reliability and sustainability.<br>Energy monitoring in support of operational efficiency is essential for modern manufacturing and facility management. Volt menders fully integrated energy &amp; operations management solution is not simply an expense, but a cost-reduction tool with many applications.</p>
<div class="abs btn about-btn">READ MORE</div>

<div class="abs" style="left:0;top:1907px;width:1200px;height:547px;background:linear-gradient(180deg,#fff,#f2f3f3)" role="img" aria-label="Faint sketch of wind turbines and solar panels"></div>
<h2 class="abs section-title" style="top:1916px">GET IN TOUCH</h2>
<div class="abs field" style="left:233px;top:2029px;width:360px;height:53px">First Name</div>
<div class="abs field" style="left:605px;top:2029px;width:360px;height:53px">Last Name</div>
<div class="abs field" style="left:233px;top:2093px;width:362px;height:54px">Email address</div>
<div class="abs field" style="left:605px;top:2093px;width:361px;height:54px">Phone Number</div>
<div class="abs field msg" style="left:233px;top:2158px;width:733px;height:116px">Message</div>
<div class="abs btn submit">SUBMIT MESSAGE</div>

<div class="abs footer-line"></div>
<div class="abs footer" role="img" aria-label="Blue-tinted photo of workers at an industrial site"></div>

<svg class="abs ficon" style="left:250px;top:2518px" viewBox="0 0 40 40"><path d="M20 11a6 6 0 0 0-6 6c0 5 6 12 6 12s6-7 6-12a6 6 0 0 0-6-6z" fill="#fff"/><circle cx="20" cy="17" r="2.2" fill="#1f4fd1"/></svg>
<div class="abs ftext" style="left:307px;top:2515px">314,At vero eos et accu<br>samus et iusto odio dimos ducimu</div>
<svg class="abs ficon" style="left:557px;top:2518px" viewBox="0 0 40 40"><path d="M14 12l4 0 2 5-2.5 1.5a10 10 0 0 0 4 4L23 20l5 2 0 4c-8 1-15-6-14-14z" fill="#fff"/></svg>
<div class="abs ftext" style="left:615px;top:2527px">1 888 888 8888</div>
<svg class="abs ficon" style="left:741px;top:2518px" viewBox="0 0 40 40"><rect x="12" y="14" width="16" height="12" rx="1" fill="#fff"/><path d="M12 15l8 6 8-6" fill="none" stroke="#1f4fd1" stroke-width="1.5"/></svg>
<div class="abs ftext" style="left:798px;top:2526px">info@voltmenders.com</div>

<nav class="abs fnav"><span>HOME</span><span>ABOUT</span><span>SERVICES</span><span>CASE STUDIES</span><span>NEWS</span><span>CONTACT US</span></nav>
<div class="abs fdivider"></div>
<div class="abs copy">Copyrights © 2021, Volt menders.All rights reserved &nbsp;| Privacy Policy &nbsp;| &nbsp;Terms and Conditions</div>
<div class="abs social"><span></span><span></span><span></span><span></span></div>

</body>
</html>
```